Customer Facing Document Design

Looking for professional design in Word for 5 Templates:

- Purchase Contract
- Sales Contract
- Packing List
- Settlement Report
- Invoice

I have attached our current designs and also some example designs that we want to look similar to. We want our company logo included on all documents. On the Purchase Order, Sales Order, Settlement Report, Invoice we also want our PQV accreditation picture and BGRL logo included.

```html
<!DOCTYPE html>
<html lang="en">
<head>
<meta charset="utf-8">
<title>VARTEK Document Templates</title>
<link href="https://fonts.googleapis.com/css2?family=Fira+Sans:wght@400;600;700&family=Open+Sans:wght@400;600;700&display=swap" rel="stylesheet">
<style>
:root{
  --backdrop:#262626;
  --paper:#ffffff;
  --head-band:#f1f1f2;
  --ink:#222222;
  --muted:#555555;
  --mark:#8c8c8e;
  --band:#9d9d9f;
  --rule:#b9b9bb;
  --frame:#808082;
  --pill:#2a2a2a;
}
*{box-sizing:border-box;margin:0;padding:0}
html,body{width:1200px;height:2191px;overflow:hidden}
body{background:var(--backdrop);position:relative;font-family:"Open Sans",Arial,sans-serif;color:var(--ink)}
.doc{position:absolute;width:515px;height:665px;background:var(--paper);overflow:hidden}
.doc--po{left:72px;top:80px}
.doc--so{left:613px;top:80px}
.doc--pl{left:72px;top:773px}
.doc--sr{left:613px;top:773px}
.doc--inv{left:343px;top:1466px}

.letterhead{position:absolute;left:0;top:0;width:100%;height:77px;background:var(--head-band);border-bottom:1.5px solid var(--frame)}
.letterhead::after{content:"";position:absolute;left:251px;bottom:-7px;border-left:5px solid transparent;border-right:5px solid transparent;border-top:6px solid var(--frame)}
.brand{position:absolute;left:20px;top:18px;display:flex;align-items:center;gap:6px}
.brand__dot{width:40px;height:40px;border-radius:50%;background:var(--mark)}
.brand__name{font-family:"Fira Sans",Arial,sans-serif;font-weight:700;font-size:24px;color:var(--mark);letter-spacing:.5px}
.company{position:absolute;left:160px;top:13px;width:195px;text-align:center;font-size:7.4px;line-height:11px;white-space:nowrap}
.company__pill{display:block;margin:0 auto 3px;width:161px;height:13px;line-height:13px;border-radius:7px;background:var(--pill);color:#fff;font-weight:700;font-size:7.6px}
.company b{font-weight:700}
.badges{position:absolute;left:376px;top:24px;display:flex;align-items:center;gap:6px}
.badge-circle{width:20px;height:20px;border-radius:50%;border:2px solid #555}
.badge-square{width:24px;height:24px;background:#6b6b6d}
.badge-sep{width:1px;height:28px;background:#555}
.assoc{display:flex;align-items:center;gap:3px;font-family:"Fira Sans",Arial,sans-serif;font-weight:700;font-size:12px;color:#555}
.assoc i{display:block;width:12px;height:12px;border-radius:50%;background:#555}

.title{position:absolute;left:0;top:106px;width:100%;text-align:center;font-family:"Fira Sans",Arial,sans-serif;font-weight:600;font-size:17.5px;letter-spacing:.2px}

.info{position:absolute;left:41px;top:134px;width:433px;height:93px;border-top:1px solid var(--frame);border-bottom:1px solid var(--frame);display:flex;font-size:7.3px;line-height:11px}
.info__party{width:217px;border-right:1px solid var(--frame);padding:13px 11px}
.info__party strong{font-weight:700;font-size:8px}
.info__meta{padding:9px 0 0 37px}
.field{display:flex}
.field dt{width:77px;font-weight:700;white-space:nowrap}
.field dd{width:100px}
.info--report .info__party{padding-top:9px}

.tbl{position:absolute;left:41px;width:433px;border-collapse:collapse;table-layout:fixed;font-size:7.4px}
.tbl th{background:var(--band);height:17px;text-align:left;padding:0 5px;font-weight:600;font-size:8px;border-left:1px solid #fff;white-space:nowrap}
.tbl th:first-child{border-left:0;text-align:center}
.tbl td{padding:0 5px;border-bottom:1px solid var(--rule);border-left:1px solid var(--rule);vertical-align:top;line-height:9px}
.tbl td:first-child{border-left:0}
.tbl--order{top:249px}
.tbl--order td{padding-top:6px;height:27px}
.tbl--order .sum td{height:30px;vertical-align:middle;padding-top:0;border-bottom:1px solid var(--frame);font-weight:700;font-size:8.2px}
.tbl .noline{border-left:0}
.right{text-align:right}
.nowrap{white-space:nowrap}

.tbl--pack{top:249px;font-size:7px}
.tbl--pack td{height:13.4px;line-height:13px;padding-top:0;white-space:nowrap}
.tbl--pack .sum td{height:22px;line-height:22px;font-weight:700;font-size:8px;border-bottom:1px solid var(--frame)}
.tbl--pack th{font-size:7.8px}

.tbl--settle{top:249px;font-size:6.2px}
.tbl--settle th{font-size:6.6px;padding:0 4px}
.tbl--settle td{height:13.4px;line-height:13px;padding:0 4px;white-space:nowrap}
.tbl--settle .sum td{font-weight:700;font-size:7.4px;border-bottom:1px solid var(--frame)}

.tbl--inv{top:249px}
.tbl--inv td{height:18px;padding-top:6px}
.tbl--inv .sum td{height:25px;vertical-align:middle;padding-top:0;font-weight:700;font-size:8.2px;border-bottom:1px solid var(--frame)}

.conditions{position:absolute;left:52px;top:350px;font-size:7.1px;line-height:12px}
.conditions h3{font-size:7.8px;font-weight:700;margin-bottom:12px}

.signbox{position:absolute;left:41px;top:561px;width:300px;height:76px;border:1.3px solid var(--frame);display:flex;font-size:7.3px;line-height:11.5px}
.signbox__party{width:140px;border-right:1px solid var(--frame);padding:8px 10px;white-space:nowrap}
.signbox__party strong,.signbox__sign{font-weight:700;font-size:7.8px}
.signbox__sign{padding:8px 20px}
.doc--inv .signbox__party{width:155px}
</style>
</head>
<body>

<!-- Purchase order -->
<section class="doc doc--po">
  <header class="letterhead">
    <div class="brand"><span class="brand__dot"></span><span class="brand__name">VARTEK</span></div>
    <div class="company"><span class="company__pill">VARTEK ALLOYS &amp; METALS, LLC</span>2418 Larkspur Circle, Fairmont Park. CA 90688<br><b>W:</b> www.vartek-am.com &nbsp;|&nbsp; <b>E:</b> SALES@VARTEK-AM.COM<br><b>T: +44 7700 900214</b></div>
    <div class="badges"><span class="badge-circle"></span><span class="badge-square"></span><span class="badge-sep"></span><span class="assoc">BGRL<i></i></span></div>
  </header>
  <h1 class="title">PURCHASE ORDER</h1>
  <div class="info">
    <div class="info__party"><strong>Vendor</strong><br>Meridian Alloys, LP<br>4410 Dunmore Street<br>Houston</div>
    <dl class="info__meta">
      <div class="field"><dt>P.O. Number:</dt><dd>MERIDIAN 060525</dd></div>
      <div class="field"><dt>P.O. Issue Date:</dt><dd>06/05/2025</dd></div>
      <div class="field"><dt>Deliver by:</dt><dd>June 2025</dd></div>
      <div class="field"><dt>Payment Terms:</dt><dd>30 Days from date of<br>receipt at Vartek</dd></div>
      <div class="field"><dt>F.O.B:</dt><dd>CPT Carriage paid to<br>VARTEK!</dd></div>
    </dl>
  </div>
  <table class="tbl tbl--order">
    <colgroup><col style="width:34px"><col style="width:63px"><col style="width:182px"><col style="width:46px"><col style="width:37px"><col style="width:71px"></colgroup>
    <tr><th>Item</th><th>Alloy</th><th>Description</th><th>Lbs</th><th>$/Lb</th><th>Total</th></tr>
    <tr><td style="text-align:center">1</td><td class="nowrap">A939 Low Zr</td><td>Solids suitable for sorting &amp; prep to vac<br>Qty - 15,000 to 20,000 Lbs</td><td>20,000</td><td>$5.50</td><td>$110,000.00</td></tr>
    <tr class="sum"><td colspan="3" class="right">Total:</td><td colspan="3" class="right" style="padding-right:10px">$110,000.00</td></tr>
  </table>
  <div class="conditions">
    <h3>Conditions:</h3>
    <ol style="list-style:none">
      <li>1. No coatings, inserts, or attachments</li>
      <li>2. Any material with inserts / attachments, payable weight is yielded recovered.</li>
      <li>3. Any material with Zr TVC, price reduction by US$1.75/lb or Buyer’s right of rejection</li>
      <li>4. Alloyed Zr max 0.022 as per chems provided, all other elements nominal</li>
    </ol>
  </div>
  <div class="signbox">
    <div class="signbox__party"><strong>Ship to:</strong><br>VARTEK A&amp;M<br>2418 LARKSPUR CIRCLE<br>FAIRMONT PARK<br>CA 90688</div>
    <div class="signbox__sign">Signed:</div>
  </div>
</section>

<!-- Sales order -->
<section class="doc doc--so">
  <header class="letterhead">
    <div class="brand"><span class="brand__dot"></span><span class="brand__name">VARTEK</span></div>
    <div class="company"><span class="company__pill">VARTEK ALLOYS &amp; METALS, LLC</span>2418 Larkspur Circle, Fairmont Park. CA 90688<br><b>W:</b> www.vartek-am.com &nbsp;|&nbsp; <b>E:</b> SALES@VARTEK-AM.COM<br><b>T: +44 7700 900214</b></div>
    <div class="badges"><span class="badge-circle"></span><span class="badge-square"></span><span class="badge-sep"></span><span class="assoc">BGRL<i></i></span></div>
  </header>
  <h1 class="title">SALES ORDER</h1>
  <div class="info">
    <div class="info__party"><strong>Vendor:</strong><br>VARTEK A&amp;M<br>2418 LARKSPUR CIRCLE<br>FAIRMONT PARK<br>CA 90688</div>
    <dl class="info__meta">
      <div class="field"><dt>S.O. Number:</dt><dd>Keystone 092325</dd></div>
      <div class="field"><dt>S.O. Issue Date:</dt><dd>09/23/2025</dd></div>
      <div class="field"><dt>Deliver by:</dt><dd>September 2025</dd></div>
      <div class="field"><dt>Payment Terms:</dt><dd>Net 30</dd></div>
      <div class="field"><dt>F.O.B:</dt><dd>DDP Belmont</dd></div>
      <div class="field"><dt>Buyer’s PO:</dt><dd><b>8554</b></dd></div>
    </dl>
  </div>
  <table class="tbl tbl--order">
    <colgroup><col style="width:34px"><col style="width:63px"><col style="width:182px"><col style="width:46px"><col style="width:37px"><col style="width:71px"></colgroup>
    <tr><th>Item</th><th>Alloy</th><th>Description</th><th>Lbs</th><th>$/Lb</th><th>Total</th></tr>
    <tr><td style="text-align:center">1</td><td class="nowrap">NX2 VQ Solids</td><td>Solids suitable for sorting &amp; prep to vac<br>Qty - 15,000 to 20,000 Lbs</td><td>1,000</td><td>$8.75</td><td>$8,750.00</td></tr>
    <tr class="sum"><td colspan="3" class="right">Total:</td><td colspan="3" class="right" style="padding-right:10px">$8,750.00</td></tr>
  </table>
  <div class="conditions">
    <h3>Conditions:</h3>
    <ol style="list-style:none">
      <li>1. No coatings, inserts, or attachments</li>
      <li>2. Any material with inserts / attachments, payable weight is yielded recovered.</li>
      <li>3. Any material with Zr TVC, price reduction by US$1.75/lb or Buyer’s right of rejection</li>
      <li>4. Alloyed Zr max 0.022 as per chems provided, all other elements nominal</li>
    </ol>
  </div>
  <div class="signbox">
    <div class="signbox__party"><strong>Buyer:</strong><br>KEYSTONE ALLOYS, LLC<br>2870 COUNTY ROAD 14<br>BELMONT<br>IL &nbsp;61099</div>
    <div class="signbox__sign">Signed:</div>
  </div>
</section>

<!-- Packing list -->
<section class="doc doc--pl">
  <header class="letterhead">
    <div class="brand"><span class="brand__dot"></span><span class="brand__name">VARTEK</span></div>
    <div class="company"><span class="company__pill">VARTEK ALLOYS &amp; METALS, LLC</span>2418 Larkspur Circle, Fairmont Park. CA 90688<br><b>W:</b> www.vartek-am.com &nbsp;|&nbsp; <b>E:</b> SALES@VARTEK-AM.COM<br><b>T: +44 7700 900214</b></div>
    <div class="badges"><span class="badge-circle"></span><span class="badge-square"></span><span class="badge-sep"></span><span class="assoc">BGRL<i></i></span></div>
  </header>
  <h1 class="title">PACKING LIST CREST TP2</h1>
  <div class="info">
    <div class="info__party" style="padding-top:9px"><strong>Vendor:</strong><br>VARTEK A&amp;M<br>2418 LARKSPUR CIRCLE<br>FAIRMONT PARK<br>CA 90688</div>
    <dl class="info__meta">
      <div class="field"><dt>P.O. Number:</dt><dd>0</dd></div>
      <div class="field"><dt>Date:</dt><dd>09/05/2025</dd></div>
      <div class="field"><dt>Via:</dt><dd>Curtain Sider</dd></div>
      <div class="field"><dt>FOB:</dt><dd>Destination</dd></div>
      <div class="field"><dt>Sales Order:</dt><dd>0</dd></div>
    </dl>
  </div>
  <table class="tbl tbl--pack">
    <colgroup><col style="width:34px"><col style="width:59px"><col style="width:82px"><col style="width:85px"><col style="width:59px"><col style="width:58px"><col style="width:56px"></colgroup>
    <tr><th>Item</th><th>BOX</th><th>Material</th><th>Packages</th><th>Gross (lbs.)</th><th>Tare (lbs.)</th><th>Net (lbs.)</th></tr>
    <tr><td>1</td><td>031925/03</td><td>Alloy 718 Turnings</td><td>bag inside stillage</td><td>303</td><td>50</td><td>253</td></tr>
    <tr><td>2</td><td>031925/04</td><td>Alloy 718 Turnings</td><td>stillage</td><td>461</td><td>55</td><td>406</td></tr>
    <tr><td>3</td><td>031925/05</td><td>Alloy 718 Turnings</td><td>stillage</td><td>242</td><td>51</td><td>191</td></tr>
    <tr><td>4</td><td>31925/06</td><td>Alloy 718 Turnings</td><td>stillage</td><td>769</td><td>54</td><td>715</td></tr>
    <tr><td>5</td><td>031925/07</td><td>Alloy 718 Turnings</td><td>stillage</td><td>281</td><td>45</td><td>236</td></tr>
    <tr><td>6</td><td>031925/08</td><td>Alloy 718 Turnings</td><td>stillage</td><td>473</td><td>49</td><td>424</td></tr>
    <tr><td>7</td><td>031925/09</td><td>Alloy 718 Turnings</td><td>stillage</td><td>698</td><td>52</td><td>646</td></tr>
    <tr><td>8</td><td>031925/10</td><td>Alloy 718 Turnings</td><td>stillage</td><td>202</td><td>51</td><td>151</td></tr>
    <tr><td>9</td><td>031925/11</td><td>Alloy 718 Turnings</td><td>stillage</td><td>682</td><td>52</td><td>630</td></tr>
    <tr><td>10</td><td>031925/12</td><td>Alloy 718 Turnings</td><td>stillage</td><td>764</td><td>51</td><td>713</td></tr>
    <tr><td>11</td><td>031925/13</td><td>Alloy 718 Turnings</td><td>stillage</td><td>281</td><td>45</td><td>236</td></tr>
    <tr><td>12</td><td>031925/14</td><td>Alloy 718 Turnings</td><td>bag inside stillage</td><td>144</td><td>10</td><td>134</td></tr>
    <tr><td>13</td><td>031925/15</td><td>Alloy 718 Turnings</td><td>stillage</td><td>301</td><td>52</td><td>249</td></tr>
    <tr><td>14</td><td>031925/16</td><td>Alloy 718 Turnings</td><td>stillage</td><td>228</td><td>50</td><td>178</td></tr>
    <tr><td>15</td><td>031925/17</td><td>Alloy 718 Turnings</td><td>stillage</td><td>225</td><td>50</td><td>175</td></tr>
    <tr><td>16</td><td>031925/18</td><td>Alloy 718 Turnings</td><td>stillage</td><td>673</td><td>44</td><td>629</td></tr>
    <tr><td>17</td><td>031925/19</td><td>Alloy 718 Turnings</td><td>stillage</td><td>102</td><td>46</td><td>56</td></tr>
    <tr><td>18</td><td>031925/20</td><td>Alloy 718 Turnings</td><td>drum</td><td>67</td><td>14</td><td>53</td></tr>
    <tr><td>19</td><td>031925/21</td><td>Alloy 718 Turnings</td><td>bag inside metal box</td><td>545</td><td>132</td><td>413</td></tr>
    <tr><td>20</td><td>031925/22</td><td>Alloy 718 Turnings</td><td>bag</td><td>77</td><td>25</td><td>52</td></tr>
    <tr><td>21</td><td>21031925/23</td><td>Alloy 625 Turnings</td><td>drum</td><td>66</td><td>10</td><td>56</td></tr>
    <tr><td>22</td><td>031925/24</td><td>Alloy 625 Turnings</td><td>bag</td><td>140</td><td>2</td><td>138</td></tr>
    <tr class="sum"><td></td><td></td><td class="noline"></td><td class="noline">Grand Total</td><td>7,724</td><td>990</td><td>6,734</td></tr>
  </table>
</section>

<!-- Settlement report -->
<section class="doc doc--sr">
  <header class="letterhead">
    <div class="brand"><span class="brand__dot"></span><span class="brand__name">VARTEK</span></div>
    <div class="company"><span class="company__pill">VARTEK ALLOYS &amp; METALS, LLC</span>2418 Larkspur Circle, Fairmont Park. CA 90688<br><b>W:</b> www.vartek-am.com &nbsp;|&nbsp; <b>E:</b> SALES@VARTEK-AM.COM<br><b>T: +44 7700 900214</b></div>
    <div class="badges"><span class="badge-circle"></span><span class="badge-square"></span><span class="badge-sep"></span><span class="assoc">BGRL<i></i></span></div>
  </header>
  <h1 class="title">SETTLEMENT REPORT</h1>
  <div class="info info--report">
    <dl class="info__party">
      <div class="field"><dt>SUPPLIER:</dt><dd style="width:110px">NORTHWAY RECYCLING</dd></div>
      <div class="field"><dt>Lot No:</dt><dd>877</dd></div>
      <div class="field"><dt>PO No.:</dt><dd></dd></div>
    </dl>
    <dl class="info__meta">
      <div class="field"><dt>DATE:</dt><dd>September 19, 2025</dd></div>
      <div class="field"><dt>RECEIVING DATE:</dt><dd>August 11, 2025</dd></div>
    </dl>
  </div>
  <table class="tbl tbl--settle">
    <colgroup><col style="width:34px"><col style="width:70px"><col style="width:119px"><col style="width:53px"><col style="width:64px"><col style="width:38px"><col style="width:55px"></colgroup>
    <tr><th>Item</th><th>Advised As:</th><th>Graded As:</th><th>Advised (Lbs)</th><th>Received (Lbs)</th><th>$ / LB</th><th></th></tr>
    <tr><td style="text-align:center">1</td><td>Alloy 718 Turnings</td><td>Alloy 718 Turnings - 1% Alum 1% Fe</td><td></td><td>284</td><td>$5.2000</td><td>$1,476.80</td></tr>
    <tr><td></td><td></td><td>Alloy 718 Turnings - 1% Alum 1% Fe</td><td></td><td>1382</td><td>$5.2000</td><td>$7,186.40</td></tr>
    <tr><td></td><td></td><td>Alloy 718 Turnings - 1% Alum 1% Fe</td><td></td><td>1390</td><td>$5.2000</td><td>$7,228.00</td></tr>
    <tr><td></td><td></td><td>Steel Turnings</td><td></td><td>556</td><td>$0.0000</td><td>$0.00</td></tr>
    <tr><td></td><td></td><td>Alloy 718 Turnings - 1% Alum 1% Fe</td><td></td><td>1340</td><td>$5.2000</td><td>$6,968.00</td></tr>
    <tr><td></td><td></td><td>Alloy 718 Turnings - 1% Alum 1% Fe</td><td></td><td>1528</td><td>$5.2000</td><td>$7,945.60</td></tr>
    <tr class="sum"><td></td><td></td><td></td><td style="padding-left:8px">0</td><td>6,480</td><td>Total</td><td>$30,804.80</td></tr>
  </table>
</section>

<!-- Sales invoice -->
<section class="doc doc--inv">
  <header class="letterhead">
    <div class="brand"><span class="brand__dot"></span><span class="brand__name">VARTEK</span></div>
    <div class="company"><span class="company__pill">VARTEK ALLOYS &amp; METALS, LLC</span>2418 Larkspur Circle, Fairmont Park. CA 90688<br><b>W:</b> www.vartek-am.com &nbsp;|&nbsp; <b>E:</b> SALES@VARTEK-AM.COM<br><b>T: +44 7700 900214</b></div>
    <div class="badges"><span class="badge-circle"></span><span class="badge-square"></span><span class="badge-sep"></span><span class="assoc">BGRL<i></i></span></div>
  </header>
  <h1 class="title">SALES INVOICE</h1>
  <div class="info">
    <div class="info__party" style="padding-top:9px"><strong>Customer:</strong><br>Summit Metal Services<br>5520 Harbor Ave<br>Cleveland<br>OH 44199</div>
    <dl class="info__meta">
      <div class="field"><dt>Contract No:</dt><dd>Summit 050725</dd></div>
      <div class="field"><dt>Date:</dt><dd>September 22, 2025</dd></div>
      <div class="field"><dt>Order No:</dt><dd>P.O. 13222</dd></div>
      <div class="field"><dt>Delivery:</dt><dd>September 22, 2025</dd></div>
      <div class="field"><dt>Payment:</dt><dd>On receipt of invoice</dd></div>
      <div class="field"><dt>Freight Terms:</dt><dd>FOB Destination</dd></div>
      <div class="field"><dt>Terms:</dt><dd>Prepaid</dd></div>
    </dl>
  </div>
  <table class="tbl tbl--inv">
    <colgroup><col style="width:32px"><col style="width:245px"><col style="width:64px"><col style="width:35px"><col style="width:57px"></colgroup>
    <tr><th>Item</th><th>Material</th><th>Lbs weight</th><th>$/Lb</th><th>$ Total</th></tr>
    <tr><td style="text-align:center">1</td><td class="nowrap">Settlement balance shortage agreed by Daniel Harlow/Steven Kerr</td><td>2,000</td><td>$1.00</td><td>$2,000.00</td></tr>
    <tr class="sum"><td colspan="2" class="right">Total:</td><td>2,000</td><td></td><td>$2,000.00</td></tr>
  </table>
  <div class="signbox">
    <div class="signbox__party"><strong>REMIT TO:</strong><br>Payment by ACH<br>Routing Number: 000 481 927<br>Account Number: 000 552 7140<br>Bank: The Lakeside Bank Company</div>
    <div class="signbox__sign">Signed:</div>
  </div>
</section>

</body>
</html>
```